Business Card for By Karel Voss

Looking to have a business card designed for my lifestyle and fitness company. My company offers personal training, online programming and nutrition advice based out of London, United Kingdom.

I'd like to see modern, sleek designs, focusing on black, matte black or matte grey. Design doesn't need to be overly descriptive as this will also be used as a personal business card. I've included my logo.

Please note that my company is no longer called "Fitness by Karel Voss" but instead "By Karel Voss", this is because of my other ventures. Therefore please don't use the "fitness by karel voss" text.

information about my company can be found at www.bykarelvoss.com

Company is also based out of London (United Kingdom) & Sydney (Australia) this could be reflected on the card.

Industry/Entity Type

Business

Contact Information for Business Card

Karel Voss
+44 7382 615027
karel@bykarelvoss.com
www.bykarelvoss.com

Font styles to use
Sans Serif

Requirements
Must have
• All contact details and inclusion of my logo.

```html
<!DOCTYPE html>
<html lang="en">
<head>
<meta charset="utf-8">
<title>By Karel Voss — Business Card</title>
<link rel="stylesheet" href="https://fonts.googleapis.com/css2?family=Montserrat:wght@300&family=Orbitron:wght@800&display=swap">
<style>
  :root {
    --page: #ffffff;
    --card-dark: #37373b;
    --card-light: #ffffff;
    --ink: #3a3a3d;
    --ink-soft: #4a4a4e;
    --on-dark: #ffffff;
  }
  html, body {
    margin: 0;
    padding: 0;
    width: 1200px;
    height: 1200px;
    overflow: hidden;
    background: var(--page);
  }
  .stage {
    position: relative;
    width: 1200px;
    height: 1200px;
  }
  .card {
    position: absolute;
    box-sizing: border-box;
  }
  .card--back {
    left: 150px;
    top: 176px;
    width: 518px;
    height: 798px;
    background: var(--card-dark);
  }
  .card--back .brand {
    position: absolute;
    left: 0;
    width: 407px;
    top: 384px;
    margin: 0;
    text-align: center;
    font-family: "Orbitron", sans-serif;
    font-weight: 800;
    font-size: 28px;
    letter-spacing: 1px;
    color: var(--on-dark);
  }
  .card--front {
    left: 557px;
    top: 238px;
    width: 516px;
    height: 797px;
    background: var(--card-light);
    box-shadow: 14px 16px 26px rgba(0, 0, 0, 0.18);
    color: var(--ink);
    font-family: "Montserrat", sans-serif;
    font-weight: 300;
  }
  .front-name {
    position: absolute;
    left: 69px;
    top: 112px;
    margin: 0;
    font-family: "Orbitron", sans-serif;
    font-weight: 800;
    font-size: 38px;
    letter-spacing: 2px;
    line-height: 1;
    white-space: nowrap;
    color: var(--ink);
  }
  .contact-line {
    position: absolute;
    left: 69px;
    margin: 0;
    white-space: nowrap;
    line-height: 1;
  }
  .contact-line--phone { top: 184px; font-size: 34px; }
  .contact-line--email { top: 239px; font-size: 26px; }
  .social-list {
    position: absolute;
    left: 70px;
    top: 369px;
    margin: 0;
    padding: 0;
    list-style: none;
  }
  .social-item {
    display: flex;
    align-factor: center;
    align-items: center;
    height: 48px;
    margin-bottom: 12px;
  }
  .social-item svg { flex: none; }
  .social-handle {
    margin-left: 30px;
    font-size: 27px;
    white-space: nowrap;
  }
  .website {
    position: absolute;
    left: 0;
    width: 516px;
    top: 680px;
    margin: 0;
    text-align: center;
    font-size: 26px;
    color: var(--ink-soft);
  }
</style>
</head>
<body>
<main class="stage">
  <section class="card card--back" aria-label="Card back">
    <p class="brand">BY KAREL VOSS</p>
  </section>

  <section class="card card--front" aria-label="Card front">
    <h1 class="front-name">KAREL VOSS</h1>
    <p class="contact-line contact-line--phone">+44 7382 615027</p>
    <p class="contact-line contact-line--email">karel@bykarelvoss.com</p>

    <ul class="social-list">
      <li class="social-item">
        <svg width="48" height="48" viewBox="0 0 48 48" aria-hidden="true"><circle cx="24" cy="24" r="22.5" fill="none" stroke="var(--ink)" stroke-width="2.5"/></svg>
        <span class="social-handle">/bykarelvoss</span>
      </li>
      <li class="social-item">
        <svg width="48" height="48" viewBox="0 0 48 48" aria-hidden="true"><circle cx="24" cy="24" r="22.5" fill="none" stroke="var(--ink)" stroke-width="2.5"/></svg>
        <span class="social-handle">/byKarelVoss</span>
      </li>
      <li class="social-item">
        <svg width="48" height="48" viewBox="0 0 48 48" aria-hidden="true"><circle cx="24" cy="24" r="22.5" fill="none" stroke="var(--ink)" stroke-width="2.5"/></svg>
        <span class="social-handle">@bykarelvoss</span>
      </li>
    </ul>

    <p class="website">www.bykarelvoss.com</p>
  </section>
</main>
</body>
</html>
```